Family Ranch with a hobby vineyard needs 2 wine labels for our first harvest

Design 2 wine labels (front and back) with the Brindor Ranch logo.
Label 1:
Sauvignon Blanc
Alc. 12.5% by Vol.
Palos Verdes Peninsula - add as the region
Year 2022
Label 2:
Cabernet Sauvignon
Alc. 13.5% by Vol.
Year 2022
For the back label design:
GOVERNMENT WARNING: (1) According to the Surgeon General, women
should not drink alcoholic beverages during pregnancy because of the risk of
birth defects. (2) Consumption of alcoholic beverages impairs your ability to
drive a car or operate machinery, and may cause health problems.
Contains Sulfates.
750ML
I just received the bottles and have attached a picture.
Look and feel
Each slider illustrates characteristics of the customer's brand and the style your logo design should communicate.

```html
<!DOCTYPE html>
<html lang="en">
<head>
<meta charset="utf-8">
<title>Brindor Ranch — Cabernet Sauvignon Label</title>
<link rel="stylesheet" href="https://fonts.googleapis.com/css2?family=Marcellus+SC&family=Josefin+Sans:wght@400;600&display=swap">
<style>
  :root {
    --page: #ffffff;
    --wine: #7a0024;
    --cream: #f4ecdc;
    --tan: #e6cf9f;
    --sky-top: #d9c37f;
    --sky-glow: #f4e3a6;
    --horizon: #c9c6a4;
    --sea: #3f6a6a;
    --shore: #5f7a3a;
  }
  * { margin: 0; padding: 0; box-sizing: border-box; }
  html, body {
    width: 1200px;
    height: 1000px;
    overflow: hidden;
    background: var(--page);
  }
  .canvas {
    position: relative;
    width: 1200px;
    height: 1000px;
  }
  .label {
    position: absolute;
    left: 246px;
    top: 146px;
    width: 708px;
    height: 708px;
    background: var(--wine);
    overflow: hidden;
  }
  .label__scene {
    position: absolute;
    inset: 0 0 auto 0;
    height: 280px;
    background:
      linear-gradient(180deg,
        var(--sky-top) 0%,
        var(--sky-glow) 35%,
        var(--horizon) 58%,
        var(--sea) 72%,
        var(--shore) 100%);
  }
  .brand {
    position: absolute;
    left: 0;
    right: 0;
    top: 40px;
    display: flex;
    flex-direction: column;
    align-items: center;
    gap: 10px;
  }
  .brand__dot {
    width: 46px;
    height: 46px;
    border-radius: 50%;
    background: var(--wine);
  }
  .brand__name {
    font-family: "Josefin Sans", sans-serif;
    font-weight: 600;
    font-size: 30px;
    letter-spacing: 0.06em;
    color: var(--wine);
    text-transform: uppercase;
  }
  .label__text {
    position: absolute;
    left: 0;
    right: 0;
    text-align: center;
  }
  .varietal {
    top: 384px;
    font-family: "Marcellus SC", serif;
    font-size: 42px;
    letter-spacing: 0.06em;
    color: var(--cream);
    text-shadow: 2px 2px 0 rgba(0, 0, 0, 0.35);
  }
  .abv {
    top: 540px;
    font-family: "Marcellus SC", serif;
    font-size: 24px;
    letter-spacing: 0.04em;
    color: var(--cream);
  }
  .region {
    top: 572px;
    font-family: "Marcellus SC", serif;
    font-size: 24px;
    letter-spacing: 0.04em;
    color: var(--tan);
  }
  .vintage {
    top: 624px;
    font-family: "Josefin Sans", sans-serif;
    font-size: 15px;
    letter-spacing: 0.08em;
    color: var(--cream);
  }
</style>
</head>
<body>
  <main class="canvas">
    <section class="label">
      <div class="label__scene" role="img" aria-label="Photo of a white coastal lighthouse with palm trees on a green bluff above the ocean at golden sunset"></div>
      <div class="brand">
        <span class="brand__dot"></span>
        <span class="brand__name">Brindor Ranch</span>
      </div>
      <h1 class="label__text varietal">Cabernet Sauvignon</h1>
      <p class="label__text abv">Alc. 13.5% by Vol.</p>
      <p class="label__text region">Palos Verdes Peninsula</p>
      <p class="label__text vintage">• YEAR 2022 •</p>
    </section>
  </main>
</body>
</html>
```